Website redesign

Looking to redesign our existing website. (quill7meadows.com.au)
New design needs to be bright, fun and have an easy flowing.
The website needs to be design with call to action.

Some examples of other websites:
fernquaylo.com
tovanmilk.com.au

We are happy with the content of our existing website.

Target Market(s)

other businesses

Industry/Entity Type

Business Service

Number of Pages Required

5+ page

Requirements
Must have
• Theme redesign
Cool animation similar to fernquaylo.com

```html
<!DOCTYPE html>
<html lang="en">
<head>
<meta charset="utf-8">
<title>Quill Meadows – Virtual Assistants</title>
<link rel="stylesheet" href="https://fonts.googleapis.com/css2?family=Catamaran:wght@300;400;600;700;800&family=Roboto:wght@300;400;500;700&display=swap">
<style>
:root{
  --blue:#12a8e0;
  --ink:#1b2433;
  --text:#3c4655;
  --line:#1b2433;
  --footer:#0c0e12;
  --white:#ffffff;
  --muted-foot:#6d7480;
}
*{box-sizing:border-box;margin:0;padding:0}
html,body{width:1200px;height:2698px;overflow:hidden}
body{position:relative;font-family:'Roboto',sans-serif;color:var(--text);
  background:linear-gradient(180deg,#ffffff 0,#eaf6fb 120px,#f3fafd 520px,#f7fbfd 900px,#e8f4fa 1400px,#f1f8fc 1700px,#f7fbfd 1980px,#eef3f6 2150px,#f2f6f8 2500px)}
.abs{position:absolute}

/* header */
.site-header{position:absolute;left:0;top:0;width:1200px;height:68px;background:var(--white);box-shadow:0 2px 10px rgba(20,60,90,.08)}
.brand{position:absolute;left:197px;top:21px;display:flex;align-items:center;gap:8px;font-family:'Catamaran',sans-serif;font-weight:800;font-size:22px;color:var(--ink)}
.brand .dot{width:14px;height:14px;border-radius:50%;background:var(--blue)}
.nav{position:absolute;left:586px;top:27px;display:flex;gap:17px;font-size:9.5px;font-weight:500;letter-spacing:.4px;color:var(--ink)}
.call-btn{position:absolute;left:944px;top:24px;width:60px;height:20px;background:var(--blue);color:#fff;font-size:8px;font-weight:700;letter-spacing:.6px;display:flex;align-items:center;justify-content:center}

/* hero */
.hero-kicker{left:196px;top:203px;font-family:'Catamaran',sans-serif;font-weight:300;font-size:30px;line-height:36px;color:var(--ink)}
.hero-title{left:196px;top:246px;font-family:'Catamaran',sans-serif;font-weight:800;font-size:47px;line-height:50px;color:var(--ink);letter-spacing:-.5px}
.btn{background:var(--blue);color:#fff;font-weight:700;letter-spacing:1px;display:flex;align-items:center;justify-content:center}
.hero-btn{left:196px;top:374px;width:125px;height:34px;font-size:11.5px}
.screen{background:linear-gradient(135deg,#ffffff 0,#f1f5f9 55%,#e4edf4 100%);box-shadow:0 10px 30px rgba(30,80,120,.15)}
.dash{left:637px;top:183px;width:360px;height:252px}
.dash-kpi{left:597px;top:371px;width:238px;height:128px}

/* intro */
.video{left:196px;top:579px;width:415px;height:325px;background:linear-gradient(120deg,#2f7fb8 0,#4aa0d6 35%,#c8d4da 60%,#8a9aa6 100%);box-shadow:0 6px 20px rgba(0,0,0,.15)}
.play{left:345px;top:680px;width:114px;height:114px;border-radius:50%;background:rgba(12,45,70,.88);border:2px solid rgba(255,255,255,.85);color:#fff;font-size:14px;letter-spacing:1px;line-height:18px;display:flex;align-items:center;justify-content:center;gap:10px}
.intro-title{left:647px;top:624px;width:360px;font-family:'Catamaran',sans-serif;font-weight:600;font-size:31px;line-height:36px;color:var(--ink)}
.intro-copy{left:647px;top:752px;width:360px;font-size:14.6px;line-height:20.3px;color:var(--text)}

/* sections */
.illus{background:radial-gradient(circle,#d3eef9 0,#e8f6fc 60%,rgba(255,255,255,0) 72%)}
.section-title{width:1200px;left:0;text-align:center;font-family:'Catamaran',sans-serif;font-weight:700;font-size:32px;color:var(--ink)}
.step-num{width:92px;height:92px;border-radius:50%;background:var(--blue);border:5px solid #fff;box-shadow:0 0 0 1px #cde9f5,0 4px 12px rgba(18,168,224,.25);color:#fff;font-family:'Catamaran',sans-serif;font-weight:300;font-size:50px;display:flex;align-items:center;justify-content:center}
.step-title{width:250px;text-align:center;color:var(--blue);font-family:'Catamaran',sans-serif;font-weight:600;font-size:13.5px}
.step-copy{width:230px;text-align:center;font-size:9.3px;line-height:13.6px;color:var(--text)}
.sub{width:1200px;left:0;text-align:center;font-size:9.6px;line-height:13.5px;color:var(--text)}
.glad{width:1200px;left:0;text-align:center;font-family:'Catamaran',sans-serif;font-weight:700;font-size:15.5px;color:var(--blue)}
.svc-list{left:196px;top:1712px;list-style:none}
.svc-list li{display:flex;align-items:center;gap:7px;font-size:13.3px;height:25.4px;color:var(--text)}
.svc-list .ring{width:13px;height:13px;border:1.5px dashed var(--blue);border-radius:50%}
.svc-cta{left:195px;top:1821px;width:390px;font-family:'Catamaran',sans-serif;font-weight:600;font-size:21px;line-height:24.5px;color:var(--ink)}
.svc-cta .hl{color:var(--blue)}
.seq{left:642px;top:1684px;width:345px;height:246px;border:1px solid #e4e9ee}
.add-step{left:844px;top:1859px;width:158px;height:88px;border:1px solid #e4e9ee}

/* quote */
.quote-band{left:0;top:1990px;width:1200px;height:510px;background:linear-gradient(180deg,rgba(220,230,236,0) 0,rgba(214,225,232,.45) 35%,rgba(214,225,232,.55) 100%)}
.quote-title{left:195px;top:2116px;font-family:'Catamaran',sans-serif;font-weight:800;font-size:40px;color:var(--ink);letter-spacing:-.5px}
.quote-lead{left:196px;top:2175px;width:290px;font-size:13.3px;line-height:16px;color:var(--text)}
.field-label{left:196px;font-size:10px;color:var(--text)}
.field-line{left:196px;width:369px;height:3px;background:var(--line)}
.submit{left:196px;top:2399px;width:369px;height:43px;font-size:14px}
.why-title{left:647px;top:2122px;font-family:'Catamaran',sans-serif;font-weight:700;font-size:27px;color:var(--blue)}
.why-lead{left:650px;top:2163px;font-size:13.5px;color:var(--text)}
.why-list{left:650px;top:2196px;list-style:none}
.why-list li{display:flex;align-items:center;gap:7px;height:25.3px;font-size:13.3px;color:var(--ink)}
.big-name{left:647px;top:2372px;font-family:'Catamaran',sans-serif;font-weight:800;font-size:60px;color:var(--ink);letter-spacing:-1px;display:flex;align-items:center;gap:16px}
.big-name .dot{width:40px;height:40px;border-radius:50%;background:var(--blue)}

/* footer */
.site-footer{left:0;top:2500px;width:1200px;height:198px;background:var(--footer)}
.f-brand{left:203px;top:2548px;font-family:'Catamaran',sans-serif;font-weight:800;font-size:22px;color:#fff;display:flex;align-items:center;gap:8px}
.f-brand .dot{width:12px;height:12px;border-radius:50%;background:var(--blue)}
.f-tag{left:203px;top:2604px;font-size:8px;color:#fff}
.f-copy{left:198px;top:2632px;font-size:7px;letter-spacing:1.4px;color:var(--muted-foot)}
.f-copy span{color:var(--blue)}
.f-made{left:198px;top:2660px;font-size:6.5px;letter-spacing:.9px;color:var(--muted-foot)}
.f-made span{color:#fff}
</style>
</head>
<body>

<header class="site-header">
  <div class="brand">QM <span class="dot"></span></div>
  <nav class="nav"><span>HOME</span><span>OUR STORY</span><span>TIPS AND TRICKS</span><span>CONTACT US</span><span>FAQ</span></nav>
  <div class="call-btn">CALL US</div>
</header>

<!-- hero -->
<svg class="abs" style="left:600px;top:110px" width="420" height="420" aria-hidden="true"><circle cx="230" cy="210" r="190" fill="none" stroke="#b9d9e8" stroke-width="1.2" stroke-dasharray="2 6"/></svg>
<div class="abs hero-kicker">VIRTUAL ASSISTANT?</div>
<div class="abs hero-title">MORE LIKE<br>VALUABLE ASSET!</div>
<div class="abs btn hero-btn">GET A QUOTE</div>
<div class="abs screen dash" role="img" aria-label="Screenshot of a sales dashboard app"></div>
<div class="abs screen dash-kpi" role="img" aria-label="Screenshot of a KPI chart panel"></div>

<!-- intro -->
<div class="abs video" role="img" aria-label="Video still of two team members standing in an office"></div>
<div class="abs play">
  <svg width="22" height="30" aria-hidden="true"><path d="M2 2 L20 15 L2 28 Z" fill="none" stroke="#fff" stroke-width="1.5"/></svg>
  <span>PLAY<br>VIDEO</span>
</div>
<h1 class="abs intro-title">Outsourcing. A big word that means big things for your business.</h1>
<p class="abs intro-copy">Virtual Assistants are the superheroes of the modern office. They can do everything your team can do on a computer at a fraction of the price! (Well, maybe not high five you when you’ve had a win, but a virtual high five is definitely on the table!)</p>

<!-- process -->
<div class="abs illus" style="left:500px;top:962px;width:200px;height:100px" role="img" aria-label="Line illustration of a computer with question mark, clock and chart icons"></div>
<h2 class="abs section-title" style="top:1092px">THE PROCESS</h2>

<div class="abs step-num" style="left:262px;top:1178px">1</div>
<div class="abs step-num" style="left:554px;top:1178px">2</div>
<div class="abs step-num" style="left:851px;top:1178px">3</div>
<svg class="abs" style="left:430px;top:1215px" width="50" height="16" aria-hidden="true"><path d="M2 10 Q25 18 46 8" fill="none" stroke="#9aa6b2" stroke-width="1"/><path d="M41 5 L46 8 L41 11" fill="none" stroke="#9aa6b2"/></svg>
<svg class="abs" style="left:735px;top:1210px" width="50" height="16" aria-hidden="true"><path d="M2 12 Q25 0 46 6" fill="none" stroke="#9aa6b2" stroke-width="1"/><path d="M41 3 L46 6 L41 9" fill="none" stroke="#9aa6b2"/></svg>

<div class="abs step-title" style="left:183px;top:1286px">Provide Your Preferred Qualifications.</div>
<div class="abs step-copy" style="left:193px;top:1307px">Set up a call with our team to specify the requirements and qualifications you’re searching for in a Virtual Assistant. This will be our checklist for your perfect assistant! From there, we’ll take care of shortlisting, testing, background checking and recruiting.</div>
<div class="abs step-title" style="left:475px;top:1286px">Endorsing the Shortlisted Candidates</div>
<div class="abs step-copy" style="left:485px;top:1307px">After the thorough vetting process, we’ll put forward the best candidate. You can then conduct the final interview on your preferred communication platform at a time that suits you. Once the schedule is set, we’ll let the candidates know!</div>
<div class="abs step-title" style="left:772px;top:1286px">Conducting the Final Interview</div>
<div class="abs step-copy" style="left:782px;top:1307px">The final interview is the perfect time to get to know the candidates. It’ll help to have a list of questions prepared that will help you pick out the chosen one!</div>

<!-- services -->
<div class="abs illus" style="left:525px;top:1429px;width:150px;height:95px" role="img" aria-label="Line illustration of a globe surrounded by light bulb, mail and smile icons"></div>
<h2 class="abs section-title" style="top:1541px">OUR SERVICES</h2>
<p class="abs sub" style="top:1588px">We’ll help you save tens (or even hundreds!) of thousands of dollars per year.<br>But what do WE actually do?</p>
<div class="abs glad" style="top:1620px">GLAD YOU ASKED!</div>

<ul class="abs svc-list">
  <li><span class="ring"></span>We recruit Virtual Assistants (a.k.a office legends!), and</li>
  <li><span class="ring"></span>Provide the tech support for these superheroes!</li>
  <li><span class="ring"></span>Set up the phone system (their own Bat Phone!)</li>
  <li><span class="ring"></span>We manage Virtual Assistants and keep them in tip-top shape!</li>
</ul>
<p class="abs svc-cta"><span class="hl">See?</span> It’s that simple! <span class="hl">The only thing to do now is to finally get started on the quote...</span> just scroll down a little more.</p>

<div class="abs screen seq" role="img" aria-label="Screenshot of an email follow-up sequence builder"></div>
<div class="abs screen add-step" role="img" aria-label="Screenshot of an add step menu"></div>

<!-- quote -->
<div class="abs quote-band" role="img" aria-label="Faint photo of a person working at an office desk"></div>
<h2 class="abs quote-title">GET A QUOTE</h2>
<p class="abs quote-lead">Fill in the form below to get a Quote for your own personal Virtual Assistant</p>
<label class="abs field-label" style="top:2230px">Your Name</label>
<div class="abs field-line" style="top:2256px"></div>
<label class="abs field-label" style="top:2280px">Your Email Address</label>
<div class="abs field-line" style="top:2306px"></div>
<label class="abs field-label" style="top:2332px">Your Message</label>
<div class="abs field-line" style="top:2375px"></div>
<svg class="abs" style="left:543px;top:2354px" width="22" height="20" aria-hidden="true"><g fill="#12a8e0"><rect x="16" y="2" width="3" height="3"/><rect x="12" y="7" width="3" height="3"/><rect x="16" y="7" width="3" height="3"/><rect x="8" y="12" width="3" height="3"/><rect x="12" y="12" width="3" height="3"/><rect x="16" y="12" width="3" height="3"/></g></svg>
<div class="abs btn submit">SUBMIT NOW</div>

<h2 class="abs why-title">IT’S QUILL MEADOWS TIME</h2>
<p class="abs why-lead">Why are we your new best outsourcing friend?</p>
<ul class="abs why-list">
  <li><svg width="14" height="14" aria-hidden="true"><circle cx="7" cy="7" r="5.5" fill="none" stroke="#12a8e0" stroke-width="1.5"/><path d="M4 7 L6.5 9.5 L11 4" fill="none" stroke="#12a8e0" stroke-width="1.6"/></svg>Your Own Virtual Assistant</li>
  <li><svg width="14" height="14" aria-hidden="true"><circle cx="7" cy="7" r="5.5" fill="none" stroke="#12a8e0" stroke-width="1.5"/><path d="M4 7 L6.5 9.5 L11 4" fill="none" stroke="#12a8e0" stroke-width="1.6"/></svg>One Invoice Per Month</li>
  <li><svg width="14" height="14" aria-hidden="true"><circle cx="7" cy="7" r="5.5" fill="none" stroke="#12a8e0" stroke-width="1.5"/><path d="M4 7 L6.5 9.5 L11 4" fill="none" stroke="#12a8e0" stroke-width="1.6"/></svg>No Super or TAX</li>
  <li><svg width="14" height="14" aria-hidden="true"><circle cx="7" cy="7" r="5.5" fill="none" stroke="#12a8e0" stroke-width="1.5"/><path d="M4 7 L6.5 9.5 L11 4" fill="none" stroke="#12a8e0" stroke-width="1.6"/></svg>Dedicated To Your Business Only</li>
  <li><svg width="14" height="14" aria-hidden="true"><circle cx="7" cy="7" r="5.5" fill="none" stroke="#12a8e0" stroke-width="1.5"/><path d="M4 7 L6.5 9.5 L11 4" fill="none" stroke="#12a8e0" stroke-width="1.6"/></svg>Dedicated Phone System</li>
  <li><svg width="14" height="14" aria-hidden="true"><circle cx="7" cy="7" r="5.5" fill="none" stroke="#12a8e0" stroke-width="1.5"/><path d="M4 7 L6.5 9.5 L11 4" fill="none" stroke="#12a8e0" stroke-width="1.6"/></svg>IT Setup and Support</li>
</ul>
<div class="abs big-name">QM <span class="dot"></span></div>

<!-- footer -->
<footer class="abs site-footer"></footer>
<div class="abs f-brand">QM <span class="dot"></span></div>
<div class="abs f-tag" style="top:2582px;font-size:8.5px">QUILL MEADOWS</div>
<div class="abs f-tag">Virtual Assistant? More Like Valuable Asset!</div>
<div class="abs f-copy">© 2019 <span>QUILL MEADOWS</span> | ALL RIGHTS RESERVED.</div>
<div class="abs f-made">Website Designed and Hosted by <span>BRIGHTLANE STUDIO - WEBSITE DESIGN</span></div>

</body>
</html>
```